Farming Operation Business Card

We need a logo designed for a Farming operation. We grow walnuts, harvest walnuts, provide orchard management for customers, lease farm ground, repair farm equipment and prune trees. This is a family owned business with two boys ages 20 & 21 working under their father. I want a design and logo hip enough for the boys but not too crazy for their conservative father. Favorite colors tend to be traditional green, navy blue and grey but not all together and open to al colors.

Let me make my concept clearer - These guys are Ranchers, Cowbolys, true blue collar workers. Up at the crack of dawn, driving a tractor, preparing the earth for harvest. These men work long hours and on big equipment to produce a out of the world walnut. They get down and dirty at their job but know how to clean up and treat a woman right. Farming is their fist love, they know nothing more then digging their hands into God's earth and pouring their sweat and blood into their harvest. Please no more designs with children holding hands in the design.

Target Market(s)

Local walnut farmers

Industry/Entity Type

Farming

Contact Information for Business Card

Callory Farms. Neil Callory. 559-731-4460On back services listed: Walnut Harvesting / Orchard Management / Orchard Leasing / Equipment Repair / Pruning

Font styles to use
Serif

Requirements
Must have
• Callory Farms
Nice to have
• A Walnut... possibly with Callory Farms logo designed in the walnut
Should not have
• NO Squirrels / No children holing hands or pictures of people

```html
<!DOCTYPE html>
<html lang="en">
<head>
<meta charset="utf-8">
<title>Callory Farms – Identity and Business Card</title>
<link rel="stylesheet" href="https://fonts.googleapis.com/css2?family=Arimo:wght@700&family=Nunito:wght@700;800&display=swap">
<style>
  :root {
    --page: #ffffff;
    --card-white: #fdfdfd;
    --bark: #4c302b;
    --leaf: #4a8a14;
    --cream: #ffffff;
    --tree-grey: #8a7d7a;
    --tree-light: #a0928f;
    --edge: #e6e6e6;
  }
  * { box-sizing: border-box; margin: 0; padding: 0; }
  html, body { width: 1200px; height: 872px; overflow: hidden; background: var(--page); }
  .board { position: relative; width: 1200px; height: 872px; }

  .wordmark {
    display: flex; align-items: center; justify-content: center; gap: 8px;
    font-family: "Nunito", sans-serif; font-weight: 800;
    color: var(--leaf);
    text-transform: uppercase;
    letter-spacing: 1px;
    white-space: nowrap;
  }
  .wordmark .mark-dot {
    flex: none; border-radius: 50%; border: 3px solid var(--bark);
  }

  /* Logo presentation square */
  .logo-tile {
    position: absolute; left: 46px; top: 246px; width: 433px; height: 434px;
    background: var(--card-white); border: 1px solid var(--edge);
    display: flex; align-items: center; justify-content: center;
  }
  .logo-tile .wordmark { font-size: 32px; }
  .logo-tile .mark-dot { width: 30px; height: 30px; }

  /* Card front */
  .card-front {
    position: absolute; left: 570px; top: 82px; width: 544px; height: 322px;
    background: var(--card-white); border: 1px solid var(--edge); overflow: hidden;
  }
  .pattern-band { position: absolute; left: 0; width: 100%; background: var(--leaf); }
  .card-front .pattern-band { top: 0; height: 32px; }
  .front-base {
    position: absolute; left: 0; top: 216px; width: 100%; height: 106px; background: var(--bark);
  }
  .logo-cutout {
    position: absolute; left: 190px; top: 86px; width: 164px; height: 164px;
    border-radius: 50%; background: var(--card-white);
  }
  .front-logo {
    position: absolute; left: 0; top: 150px; width: 100%; font-size: 22px;
  }
  .front-logo .mark-dot { width: 20px; height: 20px; border-width: 2px; }
  .contact-line {
    position: absolute; left: 0; top: 266px; width: 100%;
    display: flex; justify-content: center; align-items: center; gap: 10px;
    font-family: "Arimo", Arial, sans-serif; font-weight: 700; font-size: 19px; color: var(--cream);
  }
  .contact-line .phone { display: flex; align-items: center; gap: 3px; }
  .contact-line svg { width: 16px; height: 18px; }

  /* Card back */
  .card-back {
    position: absolute; left: 575px; top: 468px; width: 543px; height: 322px;
    background: var(--bark); overflow: hidden;
  }
  .card-back .pattern-band { bottom: 0; height: 35px; }
  .orchard-tree {
    position: absolute; left: 0; top: 52px; width: 194px; height: 235px;
    border-radius: 48% 48% 8px 8px;
    background: linear-gradient(180deg, var(--tree-light) 0%, var(--tree-grey) 100%);
    opacity: 0.85;
  }
  .back-logo {
    position: absolute; left: 404px; top: 56px; width: 130px; font-size: 10px; gap: 4px; color: var(--cream);
  }
  .back-logo .mark-dot { width: 12px; height: 12px; border-width: 2px; border-color: var(--cream); }
  .services {
    position: absolute; left: 217px; top: 92px; list-style: none;
    font-family: "Nunito", sans-serif; font-weight: 700; font-size: 17px; color: var(--cream);
  }
  .services li { display: flex; align-items: center; gap: 6px; height: 29px; }
  .services li::before {
    content: ""; width: 7px; height: 7px; border-radius: 50%; background: var(--leaf);
  }
</style>
</head>
<body>
<main class="board">

  <section class="logo-tile">
    <p class="wordmark"><span class="mark-dot"></span>Callory Farms</p>
  </section>

  <section class="card-front">
    <div class="pattern-band" role="img" aria-label="Green band with flowing walnut-shell line pattern"></div>
    <div class="front-base"></div>
    <div class="logo-cutout"></div>
    <p class="wordmark front-logo"><span class="mark-dot"></span>Callory Farms</p>
    <p class="contact-line">
      <span class="name">Neil Callory</span>
      <span class="phone">
        <svg viewBox="0 0 16 18" aria-hidden="true"><path d="M4 1 L6.5 4.5 L5 6.5 Q6 10 9 12.5 L11 11 L14.5 13.5 L13 16.5 Q10 17.5 6 13 Q1.5 8 2 3 Z" fill="none" stroke="#fff" stroke-width="1.5" stroke-linejoin="round"/></svg>
        555-208-9137
      </span>
    </p>
  </section>

  <section class="card-back">
    <div class="orchard-tree" role="img" aria-label="Illustration of a walnut tree in soft grey"></div>
    <p class="wordmark back-logo"><span class="mark-dot"></span>Callory Farms</p>
    <ul class="services">
      <li>Walnut Harvesting</li>
      <li>Orchard Management</li>
      <li>Orchard Leasing</li>
      <li>Equipment Repair</li>
      <li>Pruning</li>
    </ul>
    <div class="pattern-band" role="img" aria-label="Green band with flowing walnut-shell line pattern"></div>
  </section>

</main>
</body>
</html>
```